Pregnancy Wellbeing Coach seeks Book Cover Design

I am a former midwife who now works within alternative healthcare to support women and their families during pregnancy.
I have written a book "Quiet and Carrying Light" which is a pregnancy guide that encourages women to look "outside the box" of conventional medicine ...to find alternative solutions to difficulties that they might be experiencing. So it looks as breathing, meditative and journeying techniques, exercise, connection to nature, communication with the baby...those sort of things.
The book also is a guide for those who support the pregnant women ...the best friend, sister, mother, partner - all those who want to be involved and make a positive contribution to the transformation of the woman into motherhood ...because undoubtedly their lives will be changed by the experience.
It is my belief that we all hold an innate wisdom, the wisdom of our ancestors and that during pregnancy women are connected to the lineage of child bearers back through time ...so it is has a sacred element to it, a time of coming together ... a passing through a doorway, where life will be forever changed.
My website is : www.maevelorrimerwellbeing.example

Thank you :)

Target Market(s)

Pregnant women and those who support them during pregnancy

Industry/Entity Type

Health Care

Font styles to use
Serif
Script

Colors

Designer to choose colors to be used in the design.

Requirements
Must have
• A pregnant woman ...
• Natural World
• Title : Quiet & Carrying Light
• Subtitle : Gentle Practices to Guide A Present-Day Mother's Changing Passage Across the Months of Waiting
• Author: Maeve Lorrimer
Nice to have
• I have a feeling that nature or the natural world is important.
• And the sign of support/community
• And maybe the stars
Should not have
• No Babies
• No "highly polished women"
• No huge pregnant bellies

```html
<!DOCTYPE html>
<html lang="en">
<head>
<meta charset="utf-8">
<title>Quiet &amp; Carrying Light — Maeve Lorrimer</title>
<link href="https://fonts.googleapis.com/css2?family=Amatic+SC:wght@700&family=Antonio:wght@200&display=swap" rel="stylesheet">
<style>
  :root {
    --paper: #ffffff;
    --meadow: #a8d57a;
    --ink: #111111;
    --sky-deep: #3e5f9c;
    --sky-mid: #5b83b8;
    --lagoon: #6cc4cf;
    --sun: #f2ae42;
    --sun-soft: #e9b869;
  }
  html, body {
    margin: 0;
    padding: 0;
    width: 800px;
    height: 1200px;
    overflow: hidden;
    background: var(--paper);
  }
  .cover {
    position: relative;
    width: 800px;
    height: 1200px;
    overflow: hidden;
    background: var(--paper);
  }
  .cover-art {
    position: absolute;
    inset: 0;
  }
  .title-text,
  .author-text {
    font-family: "Amatic SC", "Comic Sans MS", cursive;
    font-weight: 700;
    fill: var(--ink);
  }
  .subtitle {
    position: absolute;
    left: 56px;
    top: 448px;
    margin: 0;
    font-family: "Antonio", "Arial Narrow", sans-serif;
    font-weight: 200;
    font-size: 33px;
    line-height: 52px;
    text-transform: uppercase;
    color: var(--ink);
    letter-spacing: -0.3px;
  }
  .subtitle span { display: block; }
</style>
</head>
<body>
<main class="cover">
  <svg class="cover-art" width="800" height="1200" viewBox="0 0 800 1200">
    <defs>
      <linearGradient id="figureTones" x1="0" y1="0" x2="0" y2="1">
        <stop offset="0" stop-color="var(--sky-deep)"/>
        <stop offset="0.3" stop-color="var(--sky-mid)"/>
        <stop offset="0.5" stop-color="var(--lagoon)"/>
        <stop offset="0.68" stop-color="var(--sun-soft)"/>
        <stop offset="1" stop-color="var(--sun)"/>
      </linearGradient>
    </defs>

    <path class="meadow-curve" d="M0 628 C 220 770, 500 850, 800 858 L 800 1200 L 0 1200 Z" fill="var(--meadow)"/>

    <path class="figure-art" role="img" aria-label="Painted silhouette of an expectant mother in blue, teal and golden tones"
          d="M640 30 C 560 30, 505 90, 505 170 C 505 300, 560 360, 540 470 C 520 580, 420 640, 330 760 C 280 830, 280 960, 330 1060 C 360 1120, 380 1170, 390 1200 L 800 1200 L 800 30 Z"
          fill="url(#figureTones)"/>

    <g class="book-title">
      <text class="title-text" x="52" y="175" font-size="190" textLength="410" lengthAdjust="spacingAndGlyphs">QUIET &amp;</text>
      <text class="title-text" x="52" y="300" font-size="150" textLength="430" lengthAdjust="spacingAndGlyphs">CARRYING</text>
      <text class="title-text" x="52" y="420" font-size="150" textLength="260" lengthAdjust="spacingAndGlyphs">LIGHT</text>
    </g>

    <text class="author-text" x="52" y="1150" font-size="190" textLength="710" lengthAdjust="spacingAndGlyphs">MAEVE LORRIMER</text>
  </svg>

  <p class="subtitle">
    <span>Gentle Practices to Guide</span>
    <span>A Present-Day Mother's</span>
    <span>Changing Passage Across</span>
    <span>the Months of Waiting</span>
  </p>
</main>
</body>
</html>
```